I have an account on Plumetry through Tanvrik, so the design will need to be built there. I already have a logo, and the design of the website should at least compliment the look of the logo. The placeholder website where the logo can be seen is at www.velmarconsulting.example. The purpose of the website at this point in time is not to drive business, but rather, to have a strong appearance and add some credibility to my already existing business.

The website should have some level of abstraction about it. I prefefer designs and shapes of images of people. The fewer people, the better. No stock photography of people standing around talking to each other.

Number of Pages Required

4 page

Requirements
Must have
• The ability to work on my existing Plume Try Account
Should not have
• Stock photography of people standing around doing "business-y" stuff. That is sooo old and played out, and is the opposite of the type of message I am trying to portray.

```html
<!DOCTYPE html>
<html lang="en">
<head>
<meta charset="utf-8">
<title>Velmar Consulting</title>
<link rel="stylesheet" href="https://fonts.googleapis.com/css2?family=Playfair+Display:wght@400;700&family=Roboto:wght@400;500;700&display=swap">
<style>
:root{
  --orange:#ef5a1c;
  --ink:#222222;
  --dark:#262626;
  --footer:#1f1f1f;
  --grey:#777777;
  --line:#e2e2e2;
  --white:#ffffff;
}
*{box-sizing:border-box;margin:0;padding:0}
html,body{width:1200px;height:4147px;overflow:hidden}
body{font-family:"Roboto",Arial,sans-serif;color:var(--ink);background:var(--white);position:relative}
.abs{position:absolute}

/* header */
.site-header{left:0;top:0;width:1200px;height:140px;background:var(--dark);z-index:3}
.brand-name{left:110px;top:38px;font-family:"Playfair Display",Georgia,serif;color:var(--white);font-size:48px;letter-spacing:2px}
.main-nav{right:110px;top:55px;display:flex;gap:28px;align-items:center}
.main-nav a{color:var(--white);text-decoration:none;font-weight:500;font-size:19px}

/* hero */
.hero{left:0;top:140px;width:1200px;height:700px;background:linear-gradient(120deg,#cfd8e2 0%,#8d99a6 40%,#4a4f57 75%,#2e3136 100%)}
.hero-title{left:110px;top:395px;color:var(--white);font-size:60px;line-height:68px;letter-spacing:6px;font-family:"Playfair Display",Georgia,serif}
.btn-quote{left:112px;top:562px;background:var(--orange);color:var(--white);font-weight:700;font-size:17px;padding:14px 26px;letter-spacing:.5px}
.arrow{width:50px;height:50px;border-radius:50%;background:var(--white);display:flex;align-items:center;justify-content:center}
.arrow.orange{background:var(--orange)}

/* section headings */
.ghost{font-family:"Playfair Display",Georgia,serif;font-size:86px;color:#ededed;letter-spacing:3px;font-weight:700;width:1200px;left:0;text-align:center}
.heading{font-family:"Playfair Display",Georgia,serif;font-weight:700;font-size:42px;color:var(--ink);width:1200px;left:0;text-align:center}

/* services */
.services-bg{left:0;top:830px;width:1200px;height:655px;background:linear-gradient(180deg,#ffffff 0%,#f6f6f6 100%)}
.service-card{width:313px;height:147px;background:var(--white);box-shadow:0 2px 12px rgba(0,0,0,.12);padding:26px 18px 0 86px}
.service-card svg{position:absolute;left:14px;top:26px}
.service-card h3{font-size:19px;font-weight:700;margin-bottom:8px}
.service-card p{font-size:14px;line-height:22px;color:var(--grey)}

/* about */
.about-photo{left:0;top:1485px;width:1200px;height:495px;background:linear-gradient(100deg,#3d3a38 0%,#6d6660 45%,#8f8379 70%,#4c4640 100%)}
.about-box{left:617px;top:1653px;width:470px;height:462px;background:var(--orange);padding:36px 50px;color:var(--white)}
.about-box h2{font-family:"Playfair Display",Georgia,serif;font-size:44px;font-weight:700;letter-spacing:1px;margin-bottom:18px}
.about-box p{font-size:14.5px;line-height:23px;margin-bottom:16px}
.btn-outline{display:inline-block;background:var(--white);color:var(--orange);font-weight:700;font-size:15px;padding:12px 28px;margin-top:6px}
.play{left:814px;top:1602px;width:70px;height:70px;border-radius:50%;background:var(--white);z-index:2}

/* blog */
.post{width:302px}
.post-image{width:302px;height:197px}
.post h3{font-size:19px;font-weight:500;margin:28px 0 10px;white-space:nowrap}
.meta{font-size:14px;color:var(--ink);display:flex;gap:28px;align-items:center}
.meta span{display:flex;gap:8px;align-items:center}
.post p{font-size:14.5px;line-height:24px;color:var(--grey);margin:18px 0 20px}
.btn-read{display:inline-block;border:2px solid #e5b8a4;color:var(--orange);font-weight:700;font-size:13.5px;padding:9px 18px}
.btn-read.filled{background:var(--orange);color:var(--white);border-color:var(--orange)}
.divider{left:110px;top:2867px;width:980px;height:2px;background:var(--line)}

/* testimonials */
.testimonial{height:207px;background:var(--white);box-shadow:0 3px 16px rgba(0,0,0,.12);border-radius:10px;padding:26px 40px}
.testimonial p{font-size:14px;line-height:24px;color:var(--grey);font-style:italic}
.person{display:flex;align-items:center;gap:16px;margin-top:16px}
.avatar{width:52px;height:52px;border-radius:50%;background:linear-gradient(135deg,#c9b3a5,#6d8aa3)}
.person b{display:block;color:var(--orange);font-size:15px;font-weight:500}
.person i{font-size:13.5px;color:var(--grey)}

/* partners */
.partners{left:0;top:3420px;width:1200px;height:260px;background:linear-gradient(180deg,#f0f0f0,#e6e6e6)}
.partner{top:3520px;font-size:28px;font-weight:500;color:#555;display:flex;align-items:center;gap:10px}
.partner i{width:22px;height:22px;background:#555;display:inline-block}

/* footer */
.site-footer{left:0;top:3700px;width:1200px;height:447px;background:var(--footer)}
.footer-brand{left:110px;top:3890px;width:270px;text-align:center;color:var(--white);font-family:"Playfair Display",Georgia,serif;font-size:48px;letter-spacing:3px}
.footer-col{color:var(--white)}
.footer-col h4{font-size:17px;font-weight:700;margin-bottom:26px}
.contact-line{display:flex;gap:18px;font-size:14px;line-height:21px;margin-bottom:22px;align-items:flex-start}
.news p{font-size:14.5px;line-height:21px;margin-bottom:12px}
.news .field{width:270px;height:34px;border:1px solid #bbb;font-size:13px;padding:8px 10px;color:#ddd}
.news .btn-sub{display:inline-block;margin-top:16px;background:var(--orange);font-size:13px;font-weight:700;padding:8px 16px}
.footer-line{top:4039px;height:1px;background:#777}
.social{left:508px;top:4022px;display:flex;gap:12px}
.social i{width:36px;height:36px;border:2px solid var(--white);border-radius:50%;background:var(--footer);display:block}
.copyright{left:0;top:4083px;width:1200px;text-align:center;font-size:14.5px;color:var(--white)}
</style>
</head>
<body>

<header class="abs site-header">
  <span class="abs brand-name">VELMAR</span>
  <nav class="abs main-nav">
    <a>HOME</a><a>ABOUT US</a><a>ENGAGE</a><a>CONTACT US</a>
    <svg width="18" height="18" viewBox="0 0 18 18"><circle cx="7.5" cy="7.5" r="5.5" fill="none" stroke="#fff" stroke-width="2.4"/><line x1="11.5" y1="11.5" x2="16.5" y2="16.5" stroke="#fff" stroke-width="2.6"/></svg>
  </nav>
</header>

<section class="abs hero" role="img" aria-label="Photo of a business meeting with a handshake across a table"></section>
<svg class="abs" style="left:0;top:740px" width="1200" height="100" viewBox="0 0 1200 100">
  <path d="M0 70 C200 20 420 20 620 48 C820 76 1000 40 1200 10 L1200 100 L0 100Z" fill="var(--orange)"/>
  <path d="M0 88 C220 40 420 42 620 66 C820 90 1000 60 1200 34 L1200 100 L0 100Z" fill="#fff"/>
</svg>
<h1 class="abs hero-title">VELMAR<br>CONSULTING</h1>
<div class="abs btn-quote">GET A QUOTE ➜</div>
<div class="abs arrow" style="left:32px;top:455px"><svg width="14" height="18" viewBox="0 0 14 18"><path d="M11 2 L4 9 L11 16" fill="none" stroke="var(--orange)" stroke-width="3"/></svg></div>
<div class="abs arrow orange" style="left:1118px;top:455px"><svg width="14" height="18" viewBox="0 0 14 18"><path d="M3 2 L10 9 L3 16" fill="none" stroke="#fff" stroke-width="3"/></svg></div>

<section class="abs services-bg"></section>
<div class="abs ghost" style="top:920px">OUR SOLUTIONS</div>
<h2 class="abs heading" style="top:946px">OUR SERVICES</h2>

<div class="abs service-card" style="left:110px;top:1056px"><svg width="60" height="60" viewBox="0 0 60 60"><rect x="8" y="14" width="44" height="36" fill="none" stroke="var(--orange)" stroke-width="2.5"/><path d="M14 44 L26 28 L34 36 L46 20" fill="none" stroke="var(--orange)" stroke-width="2.5"/></svg><h3>Brand Strategy</h3><p>At vero eos et accusamus et iusto odio dignissimos ducimus qui blanditiis praes...</p></div>
<div class="abs service-card" style="left:443px;top:1056px"><svg width="60" height="60" viewBox="0 0 60 60"><rect x="8" y="10" width="44" height="30" fill="none" stroke="var(--orange)" stroke-width="2.5"/><rect x="18" y="40" width="24" height="12" fill="none" stroke="var(--orange)" stroke-width="2.5"/><circle cx="30" cy="25" r="7" fill="none" stroke="var(--orange)" stroke-width="2.5"/></svg><h3>Brand Identity</h3><p>At vero eos et accusamus et iusto odio dignissimos ducimus qui blanditiis praes...</p></div>
<div class="abs service-card" style="left:777px;top:1056px"><svg width="60" height="60" viewBox="0 0 60 60"><path d="M8 14 L30 20 L52 14 L52 48 L30 54 L8 48Z M30 20 L30 54" fill="none" stroke="var(--orange)" stroke-width="2.5"/></svg><h3>Brand Guidelines</h3><p>At vero eos et accusamus et iusto odio dignissimos ducimus qui blanditiis praes...</p></div>
<div class="abs service-card" style="left:110px;top:1225px"><svg width="60" height="60" viewBox="0 0 60 60"><circle cx="30" cy="30" r="20" fill="none" stroke="var(--orange)" stroke-width="2.5"/><path d="M30 14 L30 30 L42 38" fill="none" stroke="var(--orange)" stroke-width="2.5"/></svg><h3>Creative Direction</h3><p>At vero eos et accusamus et iusto odio dignissimos ducimus qui blanditiis praes...</p></div>
<div class="abs service-card" style="left:443px;top:1225px"><svg width="60" height="60" viewBox="0 0 60 60"><rect x="6" y="12" width="48" height="32" fill="none" stroke="var(--orange)" stroke-width="2.5"/><line x1="6" y1="20" x2="54" y2="20" stroke="var(--orange)" stroke-width="2.5"/><line x1="22" y1="52" x2="38" y2="52" stroke="var(--orange)" stroke-width="2.5"/></svg><h3>Website Design</h3><p>At vero eos et accusamus et iusto odio dignissimos ducimus qui blanditiis praes...</p></div>
<div class="abs service-card" style="left:777px;top:1225px"><svg width="60" height="60" viewBox="0 0 60 60"><circle cx="30" cy="22" r="9" fill="none" stroke="var(--orange)" stroke-width="2.5"/><path d="M12 52 C14 38 46 38 48 52" fill="none" stroke="var(--orange)" stroke-width="2.5"/></svg><h3>Customer Insights</h3><p>At vero eos et accusamus et iusto odio dignissimos ducimus qui blanditiis praes...</p></div>

<section class="abs about-photo" role="img" aria-label="Photo of a team working on laptops around a table"></section>
<svg class="abs" style="left:0;top:1880px" width="1200" height="110" viewBox="0 0 1200 110">
  <path d="M0 70 C200 20 420 10 640 50 C840 86 1020 70 1200 40 L1200 110 L0 110Z" fill="#fff"/>
</svg>
<div class="abs about-box">
  <h2>ABOUT US</h2>
  <p>Lorem ipsum dolor sit amet, consectetur adipiscing elit, sed do eiusmod tempor incididunt.</p>
  <p>Ut labore et dolore magna aliqua. Ut enim ad minim veniam, quis nostrud exercitation ullamco laboris nisi ut aliquip ex ea commodo consequat. Duis aute irure dolor in reprehenderit in voluptate velit esse cillum dolore eu fugiat nulla pariatur. Excepteur sint occaecat cupidatat non proident, sunt in culpa qui officia deserunt mollit anim id est laborum.</p>
  <span class="btn-outline">READ MORE ➜</span>
</div>
<div class="abs play"><svg width="70" height="70" viewBox="0 0 70 70"><path d="M28 22 L50 35 L28 48Z" fill="var(--orange)"/></svg></div>

<div class="abs ghost" style="top:2200px">LATEST BLOG POST</div>
<h2 class="abs heading" style="top:2226px">LATEST BLOG POST</h2>

<article class="abs post" style="left:110px;top:2328px">
  <div class="post-image" role="img" aria-label="Photo of colleagues greeting in an office" style="background:linear-gradient(135deg,#e7ecf0,#9aa7b3)"></div>
  <h3>Nemo enim ipsam voluptatem.</h3>
  <div class="meta"><span><svg width="14" height="14"><rect x="1" y="2" width="12" height="11" fill="var(--orange)"/></svg>Feb 30, 2019</span><span><svg width="14" height="14"><circle cx="7" cy="4" r="3.5" fill="var(--orange)"/><path d="M1 14 C2 7 12 7 13 14Z" fill="var(--orange)"/></svg>Jon Dale</span></div>
  <p>Lorem ipsum dolor sit amet, consectetur adip iscing elit, sed do eiusmod tempor incididunt ut labore et dolore magna aliqua.</p>
  <span class="btn-read">READ MORE ➜</span>
</article>
<article class="abs post" style="left:448px;top:2328px">
  <div class="post-image" role="img" aria-label="Photo of hands reviewing charts on a desk" style="background:linear-gradient(135deg,#f2f2f2,#b7bcc2)"></div>
  <h3>At vero eos et accusamus iusto</h3>
  <div class="meta"><span><svg width="14" height="14"><rect x="1" y="2" width="12" height="11" fill="var(--orange)"/></svg>Feb 30, 2019</span><span><svg width="14" height="14"><circle cx="7" cy="4" r="3.5" fill="var(--orange)"/><path d="M1 14 C2 7 12 7 13 14Z" fill="var(--orange)"/></svg>Jon Dale</span></div>
  <p>Lorem ipsum dolor sit amet, consectetur adip iscing elit, sed do eiusmod tempor incididunt ut labore et dolore magna aliqua.</p>
  <span class="btn-read filled">READ MORE ➜</span>
</article>
<article class="abs post" style="left:785px;top:2328px">
  <div class="post-image" role="img" aria-label="Photo of two people working at a laptop" style="background:linear-gradient(135deg,#d5dbe2,#4d5661)"></div>
  <h3>Ut enim ad minima veniam quis</h3>
  <div class="meta"><span><svg width="14" height="14"><rect x="1" y="2" width="12" height="11" fill="var(--orange)"/></svg>Feb 30, 2019</span><span><svg width="14" height="14"><circle cx="7" cy="4" r="3.5" fill="var(--orange)"/><path d="M1 14 C2 7 12 7 13 14Z" fill="var(--orange)"/></svg>Jon Dale</span></div>
  <p>Lorem ipsum dolor sit amet, consectetur adip iscing elit, sed do eiusmod tempor incididunt ut labore et dolore magna aliqua.</p>
  <span class="btn-read">READ MORE ➜</span>
</article>

<div class="abs divider"></div>

<div class="abs ghost" style="top:2966px">TESTIMONIALS</div>
<h2 class="abs heading" style="top:2966px">WHAT SAYS OUR CLIENTS</h2>
<div class="abs testimonial" style="left:130px;top:3097px;width:445px">
  <p>“ Lorem ipsum dolor sit amet, consectetur adipiscing elit, sed do eiusmod tempor incididunt ut labore et dolore magna aliqua. Ut enim ad minim veniam, quis nostrud exercitation ”</p>
  <div class="person"><div class="avatar" role="img" aria-label="Client portrait"></div><div><b>Mira Holt,</b><i>Creative Manager at ABC.</i></div></div>
</div>
<div class="abs testimonial" style="left:622px;top:3097px;width:456px">
  <p>“ Lorem ipsum dolor sit amet, consectetur adipiscing elit, sed do eiusmod tempor incididunt ut labore et dolore magna aliqua. Ut enim ad minim veniam, quis nostrud exercitation ”</p>
  <div class="person"><div class="avatar" role="img" aria-label="Client portrait"></div><div><b>Evan Tarrow,</b><i>Creative Manager at ABC.</i></div></div>
</div>
<div class="abs arrow" style="left:30px;top:3175px;box-shadow:0 2px 8px rgba(0,0,0,.2)"><svg width="14" height="18" viewBox="0 0 14 18"><path d="M11 2 L4 9 L11 16" fill="none" stroke="var(--orange)" stroke-width="3"/></svg></div>
<div class="abs arrow orange" style="left:1118px;top:3175px"><svg width="14" height="18" viewBox="0 0 14 18"><path d="M3 2 L10 9 L3 16" fill="none" stroke="#fff" stroke-width="3"/></svg></div>

<section class="abs partners"></section>
<div class="abs partner" style="left:115px"><i></i>Brightfield</div>
<div class="abs partner" style="left:345px">Northwick</div>
<div class="abs partner" style="left:530px"><i></i>Corvale</div>
<div class="abs partner" style="left:735px"><i></i>Ostrel</div>
<div class="abs partner" style="left:918px"><i></i>Mailvane</div>
<svg class="abs" style="left:0;top:3620px" width="1200" height="90" viewBox="0 0 1200 90">
  <path d="M0 40 C180 80 360 90 560 60 C760 30 960 10 1200 34 L1200 90 L0 90Z" fill="var(--orange)"/>
  <path d="M0 62 C180 96 380 100 580 76 C780 52 980 40 1200 58 L1200 90 L0 90Z" fill="var(--footer)"/>
</svg>

<footer class="abs site-footer"></footer>
<div class="abs footer-brand">VELMAR</div>
<div class="abs footer-col" style="left:455px;top:3800px">
  <h4>CONTACT US</h4>
  <div class="contact-line"><svg width="14" height="18"><path d="M7 17 C2 10 1 8 1 6 A6 6 0 0 1 13 6 C13 8 12 10 7 17Z" fill="#fff"/></svg><span>48 Harbour Lane, Eastmoor<br>Westvale, WV 2041</span></div>
  <div class="contact-line"><svg width="14" height="16"><path d="M2 1 L6 1 L7 5 L5 7 C6 9 8 11 10 12 L12 10 L14 12 L14 15 C7 15 1 9 1 2Z" fill="#fff"/></svg><span>(+100) 555 0147</span></div>
  <div class="contact-line"><svg width="16" height="14"><rect x="1" y="2" width="14" height="10" fill="#fff"/><path d="M1 2 L8 8 L15 2" fill="none" stroke="#1f1f1f" stroke-width="1.5"/></svg><span>info@velmarconsulting.example</span></div>
</div>
<div class="abs footer-col news" style="left:822px;top:3800px">
  <h4>NEWSLETTER SUBSCRIPTION</h4>
  <p>Register your Email Address to get more<br>Information about us</p>
  <div class="field">Email Address</div>
  <span class="btn-sub">SUBSCRIBE</span>
</div>
<div class="abs footer-line" style="left:110px;width:390px"></div>
<div class="abs footer-line" style="left:700px;width:390px"></div>
<div class="abs social" aria-label="Social links"><i></i><i></i><i></i><i></i></div>
<div class="abs copyright">Copyrights © 2019 Velmar Consulting.&nbsp; All Rights Reserved &nbsp;&nbsp;|&nbsp;&nbsp; Privacy Policy.</div>

</body>
</html>
```